Business Card Design

We develop / design / build affordable housing throughout the state of Illinois.

Target Market(s)

non profit organizations and other developers / professionals in my industry

Industry/Entity Type

Business

Contact Information for Business Card

Verdell Ridge Construction, LLC
General Contracting
Marisol K Thornbury, CEO
418 North Wendell P Ashcroft Avenue, Suite 307
Elmhurst, IL 60126
630-555-0148
mkt@buildverdellridge.com

```html
<!DOCTYPE html>
<html lang="en">
<head>
<meta charset="utf-8">
<title>Verdell Ridge Construction – Business Card</title>
<link href="https://fonts.googleapis.com/css2?family=Tinos:ital,wght@0,400;0,700;1,700&display=swap" rel="stylesheet">
<style>
  :root {
    --backdrop: #0c0c0c;
    --card-white: #ffffff;
    --ink: #111111;
    --muted-ink: #555555;
    --gold-light: #f3e4c4;
    --gold-mid: #e2c79a;
    --gold-deep: #c9a373;
    --gold-shade: #b88f62;
  }
  html, body {
    margin: 0;
    padding: 0;
    width: 1200px;
    height: 1190px;
    overflow: hidden;
    background: var(--backdrop);
    font-family: "Tinos", "Times New Roman", serif;
  }
  .canvas {
    position: relative;
    width: 1200px;
    height: 1190px;
  }
  .card {
    position: absolute;
    left: 130px;
    width: 940px;
    height: 537px;
    overflow: hidden;
  }
  .card--front { top: 40px; background: var(--card-white); }
  .card--back  { top: 613px; }

  .wood-finish {
    background: linear-gradient(100deg, var(--gold-deep) 0%, var(--gold-mid) 30%, var(--gold-light) 52%, var(--gold-mid) 72%, var(--gold-shade) 100%);
  }
  .side-band {
    position: absolute;
    left: 0; top: 0;
    width: 68px;
    height: 100%;
  }
  .divider-bar {
    position: absolute;
    left: 68px; right: 0;
    top: 280px;
    height: 18px;
    background: linear-gradient(90deg, var(--gold-shade) 0%, var(--gold-light) 35%, var(--gold-mid) 65%, var(--gold-deep) 100%);
  }
  .brand-mark {
    position: absolute;
    left: 105px;
    top: 110px;
    display: flex;
    align-items: center;
    gap: 10px;
    font-size: 16px;
    color: var(--muted-ink);
  }
  .brand-mark__square {
    width: 26px;
    height: 26px;
    background: var(--muted-ink);
  }
  .front-heading {
    position: absolute;
    right: 93px;
    top: 62px;
    text-align: right;
    font-weight: 700;
    color: var(--ink);
  }
  .company-name { font-size: 35px; line-height: 1.2; }
  .service-line { font-size: 30px; line-height: 1.4; }
  .person-name {
    position: absolute;
    right: 93px;
    top: 212px;
    font-size: 40px;
    font-weight: 700;
    color: var(--ink);
  }
  .contact-block {
    position: absolute;
    right: 26px;
    top: 330px;
    text-align: right;
    font-size: 27px;
    line-height: 1.38;
    color: var(--ink);
  }
  .contact-block b { font-weight: 700; }

  .back-heading {
    position: absolute;
    left: 0; right: 0;
    top: 195px;
    text-align: center;
    font-weight: 700;
    font-style: italic;
    color: var(--ink);
  }
  .back-heading .company-name { font-size: 40px; line-height: 1.2; }
  .back-heading .service-line { font-size: 34px; line-height: 2.3; }
</style>
</head>
<body>
<main class="canvas">
  <section class="card card--front" aria-label="Business card front">
    <div class="side-band wood-finish" role="img" aria-label="Gold wood-grain side band"></div>
    <div class="divider-bar" role="img" aria-label="Gold wood-grain divider bar"></div>
    <div class="brand-mark">
      <span class="brand-mark__square"></span>
      <span>Verdell Ridge Construction</span>
    </div>
    <div class="front-heading">
      <div class="company-name">Verdell Ridge Construction, LLC</div>
      <div class="service-line">General Contracting</div>
    </div>
    <div class="person-name">Marisol K Thornbury</div>
    <address class="contact-block" style="font-style:normal">
      <div><b>Address:</b>418 North Wendell P Ashcroft Avenue,</div>
      <div>Suite 307 Elmhurst, IL 60126</div>
      <div><b>Phone:</b>630-555-0148</div>
      <div><b>E-mai:</b>mkt@buildverdellridge.com</div>
    </address>
  </section>

  <section class="card card--back wood-finish" role="img" aria-label="Business card back with gold wood-grain finish">
    <div class="back-heading">
      <div class="company-name">Verdell Ridge Construction, LLC</div>
      <div class="service-line">General Contracting</div>
    </div>
  </section>
</main>
</body>
</html>
```